Get Up to $ 500,000 in Business Capital within 48 hours

design a flyer offering business capital to businesses. The flyer is going to be mailed to business owners and the flyer needs to immediately capture their attention.
The flyer needs to be bold and professional and really stand-out.
pppppppppppppppppppppppppppppppppppppppppppppppppppppppppppppppppppppppppppppppppppppppppppppppppppppppppppppppppppppppppppppppppppppppppppppppppppppppppppppppppppppppppppppppppppppppppppppppppppppppppppppppppppppppppppppppppppppp

Target Market(s)

business owners

Font styles to use
Serif

Requirements
Must have
• Apply online in minutes at PellarCapital.example or call 800-GRAB-NOW
Nice to have
• We fund almost every business type. Not a business loan, receive a cash advance on your future sales.

```html
<!DOCTYPE html>
<html lang="en">
<head>
<meta charset="utf-8">
<title>PellarCapital Business Capital Flyer</title>
<link rel="stylesheet" href="https://fonts.googleapis.com/css2?family=Oswald:wght@600;700&family=Montserrat:wght@600;700;800&display=swap">
<style>
  :root {
    --navy: #1e3382;
    --sky: #4aa7e0;
    --cyan: #1fa3dc;
    --grey: #7b7b7b;
    --grey-dark: #555759;
    --ink: #3a3a3c;
    --paper: #ffffff;
    --backdrop: #eeeeee;
    --rule: #c9c9c9;
  }
  * { box-sizing: border-box; margin: 0; padding: 0; }
  html, body {
    width: 1200px; height: 2367px; overflow: hidden;
    background: var(--backdrop);
  }
  .flyer {
    position: absolute; left: 52px; top: 473px;
    width: 755px; height: 980px;
    transform: scale(1.45); transform-origin: 0 0;
    background: var(--paper); overflow: hidden;
    font-family: "Montserrat", Arial, sans-serif;
    box-shadow: 0 6px 20px rgba(0,0,0,.18);
  }
  .brand {
    position: absolute; left: 42px; top: 38px;
    font: 700 38px/1 "Montserrat", Arial, sans-serif;
    color: var(--sky); letter-spacing: -1px;
  }
  .hero-band { position: absolute; left: 0; top: 96px; width: 420px; height: 266px; }
  .headline {
    position: absolute; left: 42px; top: 130px;
    font: 700 62px/62px "Oswald", "Arial Narrow", sans-serif;
    color: var(--paper); text-transform: uppercase;
  }
  .headline .lead { color: var(--sky); display: block; }
  .photo { position: absolute; left: 330px; top: -40px; width: 540px; height: 540px; }
  .offer {
    position: absolute; left: 42px; top: 385px;
    font: 700 21px/28px "Montserrat", Arial, sans-serif; color: var(--ink);
  }
  .offer .amount { color: var(--navy); }
  .rule { position: absolute; left: 42px; top: 466px; width: 428px; height: 1px; background: var(--rule); }
  .rule::before { content: ""; position: absolute; left: 0; top: -2px; width: 40px; height: 5px; background: var(--navy); }
  .qualify {
    position: absolute; left: 42px; top: 495px; width: 408px; height: 88px;
    background: var(--grey); color: var(--paper);
    font: 700 28px/34px "Montserrat", Arial, sans-serif; padding: 9px 16px;
  }
  .big-figure {
    position: absolute; left: 458px; top: 486px;
    font: 700 86px/100px "Oswald", "Arial Narrow", sans-serif; color: var(--navy);
    letter-spacing: -1px;
  }
  .perk { position: absolute; top: 597px; display: flex; align-items: center; gap: 14px; }
  .perk svg { width: 86px; height: 86px; flex: none; }
  .perk p { font: 700 22px/28px "Montserrat", Arial, sans-serif; color: var(--grey-dark); text-transform: uppercase; }
  .perk-credit { left: 42px; }
  .perk-form { left: 412px; }
  .perk-divider { position: absolute; left: 377px; top: 612px; height: 54px; border-left: 2px dotted #aaa; }
  .benefits {
    position: absolute; left: 42px; top: 705px; width: 668px; height: 176px;
    border: 2px solid #bdbdbd; border-radius: 20px;
    box-shadow: 0 10px 8px -8px rgba(0,0,0,.25);
    display: flex;
  }
  .benefit { flex: 1; display: flex; flex-direction: column; align-items: center; padding-top: 10px; position: relative; }
  .benefit + .benefit::before {
    content: ""; position: absolute; left: 0; top: 36px; height: 90px; border-left: 2px dotted #aaa;
  }
  .benefit svg { width: 86px; height: 86px; }
  .benefit p { margin-top: 10px; text-align: center; font: 700 14.5px/17px "Montserrat", Arial, sans-serif; color: var(--ink); }
  .footer { position: absolute; left: 0; top: 905px; width: 755px; height: 75px; }
  .footer svg { position: absolute; inset: 0; }
  .apply {
    position: absolute; left: 42px; top: 915px;
    font: 700 21px/25px "Montserrat", Arial, sans-serif; color: var(--paper);
  }
  .contact {
    position: absolute; left: 250px; top: 930px; display: flex; align-items: center; gap: 8px;
    font: 700 18px/26px "Montserrat", Arial, sans-serif; color: var(--paper);
  }
  .contact svg { width: 22px; height: 22px; }
  .contact .web { margin-left: 8px; }
</style>
</head>
<body>
<main class="flyer">
  <div class="brand">PELLARCAPITAL</div>

  <svg class="hero-band" viewBox="0 0 420 266" aria-hidden="true">
    <polygon points="0,0 125,0 112,14 0,14" fill="#4aa7e0"/>
    <polygon points="0,10 420,10 420,266 0,266" fill="#1e3382"/>
    <polygon points="0,250 100,250 115,266 0,266" fill="#4aa7e0"/>
    <polygon points="100,250 112,250 127,266 115,266" fill="#ffffff"/>
  </svg>

  <h1 class="headline"><span class="lead">Need</span>Business<br>Capital?</h1>

  <svg class="photo" viewBox="0 0 540 540">
    <defs>
      <linearGradient id="photoTone" x1="0" y1="0" x2="0.4" y2="1">
        <stop offset="0" stop-color="#e9eef4"/>
        <stop offset="0.5" stop-color="#c7ccd6"/>
        <stop offset="1" stop-color="#23273a"/>
      </linearGradient>
    </defs>
    <circle cx="262" cy="270" r="255" fill="#1e3382"/>
    <circle cx="270" cy="270" r="248" fill="#ffffff"/>
    <circle cx="274" cy="270" r="238" fill="url(#photoTone)" role="img" aria-label="Photo of three smiling business people in dark suits standing in a bright office"/>
  </svg>

  <p class="offer">Get Up to <span class="amount">$ 500,000</span> in<br>Business Capital within 48 hours</p>
  <div class="rule"></div>

  <div class="qualify">You can qualify for up<br>to in just 24 hours.</div>
  <div class="big-figure">500,000</div>

  <div class="perk perk-credit">
    <svg viewBox="0 0 86 86" aria-hidden="true">
      <circle cx="43" cy="43" r="40" fill="none" stroke="#1e3382" stroke-width="5"/>
      <circle cx="46" cy="32" r="13" fill="#555759"/>
      <text x="46" y="38" font-family="Montserrat, sans-serif" font-weight="700" font-size="17" fill="#fff" text-anchor="middle">$</text>
      <rect x="18" y="50" width="8" height="18" fill="#1e3382"/>
      <path d="M28 52 h16 q6 0 6 5 h-14 M28 66 h22 l16 -12 q-4 -5 -9 -1 l-9 6" fill="none" stroke="#555759" stroke-width="5" stroke-linejoin="round"/>
    </svg>
    <p>No minimum<br>credit score</p>
  </div>
  <div class="perk-divider"></div>
  <div class="perk perk-form">
    <svg viewBox="0 0 86 86" aria-hidden="true">
      <circle cx="43" cy="43" r="40" fill="none" stroke="#1e3382" stroke-width="5"/>
      <path d="M29 20 h20 l10 10 v36 h-30 z" fill="#555759"/>
      <path d="M49 20 v10 h10" fill="#8a8a8a"/>
      <path d="M35 40 h18 M35 47 h18 M35 54 h18" stroke="#fff" stroke-width="3"/>
    </svg>
    <p>Simple 1 page<br>application</p>
  </div>

  <section class="benefits">
    <div class="benefit">
      <svg viewBox="0 0 86 86" aria-hidden="true">
        <circle cx="43" cy="43" r="40" fill="none" stroke="#1fa3dc" stroke-width="5"/>
        <rect x="35" y="22" width="16" height="9" rx="2" fill="none" stroke="#555759" stroke-width="4"/>
        <rect x="20" y="30" width="46" height="32" rx="4" fill="#555759"/>
        <rect x="20" y="43" width="46" height="3" fill="#ffffff"/>
        <rect x="40" y="40" width="6" height="9" fill="#ffffff"/>
      </svg>
      <p>Not a business loan,get<br>a cash advance today<br>on your future sales.</p>
    </div>
    <div class="benefit">
      <svg viewBox="0 0 86 86" aria-hidden="true">
        <circle cx="43" cy="43" r="40" fill="none" stroke="#1fa3dc" stroke-width="5"/>
        <rect x="26" y="18" width="32" height="46" fill="#fff" stroke="#555759" stroke-width="3"/>
        <rect x="29" y="21" width="22" height="10" fill="#555759"/>
        <text x="40" y="29" font-family="Montserrat, sans-serif" font-weight="700" font-size="8" fill="#fff" text-anchor="middle">LOAN</text>
        <path d="M31 37 h22 M31 43 h22 M31 49 h16 M31 55 h12" stroke="#555759" stroke-width="2.5"/>
        <path d="M62 30 l-14 22 l-3 5 l5 -3 l14 -21 z" fill="#1e3382"/>
      </svg>
      <p>Convenient alternative<br>to a bank loan.</p>
    </div>
    <div class="benefit">
      <svg viewBox="0 0 86 86" aria-hidden="true">
        <circle cx="43" cy="43" r="40" fill="none" stroke="#1fa3dc" stroke-width="5"/>
        <rect x="18" y="24" width="44" height="32" rx="2" fill="#555759"/>
        <path d="M22 30 h10 v6 h-10 z M36 31 h20 M36 36 h20 M22 42 h34 M22 48 h24" stroke="#fff" stroke-width="2.5" fill="none"/>
        <circle cx="60" cy="46" r="6" fill="#1e3382"/>
        <path d="M51 64 v-6 q0 -6 9 -6 q9 0 9 6 v6 z" fill="#1e3382"/>
      </svg>
      <p>We fund virtually<br>every type of<br>business.</p>
    </div>
  </section>

  <div class="footer">
    <svg viewBox="0 0 755 75" aria-hidden="true">
      <rect width="755" height="75" fill="#555759"/>
      <polygon points="0,0 245,0 272,75 0,75" fill="#1e3382"/>
      <polygon points="245,0 250,0 277,75 272,75" fill="#ffffff"/>
    </svg>
  </div>
  <p class="apply">Apply online in<br>minutes</p>
  <p class="contact">
    <svg viewBox="0 0 24 24" aria-hidden="true"><path d="M6.6 3.5 l3 3.6 -1.8 2.2 q1.6 3.6 5 5.2 l2.2 -1.8 3.6 3 -1.6 3 q-9.5 -0.6 -13.5 -12.5 z" fill="#4aa7e0"/></svg>
    call 800-GRAB-NOW
    <svg class="web" viewBox="0 0 24 24" aria-hidden="true"><circle cx="12" cy="12" r="9" fill="none" stroke="#4aa7e0" stroke-width="2"/><path d="M3 12 h18 M12 3 q-6 9 0 18 q6 -9 0 -18" fill="none" stroke="#4aa7e0" stroke-width="2"/></svg>
    PellarCapital.example
  </p>
</main>
</body>
</html>
```